Graphics Design of Physics Book

Hi
Size : 8" x 11.25"
We are education book Publication Company and would like to have book cover for "Physics" it has 4 volumes. All 4 having the same color scheme and design except the volume no.
Blue is my personal favorite but u can use any color. Want to have a band at the bottom of the cover to place our Logo “VORLIN Education” a PDF of the same is attached, or you can place logo anywhere according to ur design.
I need “Physics” as title of the book to be visible prominently.
And volume and volume no. should also be Visible and eye catching I prefer a Graphic to enhance the Volume No.
A background pattern can also be a option (it should be vector form so that color can be change later)
Please do not offer any cut and paste design I need very professional presentation.
Volume and Number can be in metallic 3D (CMYK) effect.
only Professional presentation will get feedback.
I have provided a sample artwork for reference do not follow it but can be a reference what I needed !

Target Market(s)

Students Class 9th to 12th

Industry/Entity Type

Education

Font styles to use
Serif

Colors
3176b5
0555a3
85abd2
cadf82
abd036
9bcb3c

Requirements
Must have
• Eye catching.
• “Physics” as title of the book to be visible prominently.
• volume and volume no. should also be Visible and eye catching
• I prefer a Graphic to enhance the Volume No.
• Icons for
• 1. Questions and answers
• 2. Theory Notes
• 3. Tips & Tricks
• 4. Previous Year's Reference Questions
• 5. Covers Complete Syllabus
Nice to have
• decent seamless background or metallic 3d effect (not to be print in special Ink) design should only be in CMYK.
Should not have
• Physics related Pictures or Icons (Specially E=mc2) or any scientist photograph or I Need pure graphic design

```html
<!DOCTYPE html>
<html lang="en">
<head>
<meta charset="utf-8">
<title>Physics Vol 1 — Book Cover</title>
<link rel="stylesheet" href="https://fonts.googleapis.com/css2?family=Alfa+Slab+One&family=Roboto+Condensed:wght@700&family=Roboto:wght@700&display=swap">
<style>
  :root{
    --navy:#1c2a48;
    --navy-deep:#19243f;
    --blue-mid:#22468f;
    --blue-bright:#1a4fa0;
    --blue-sky:#0a56a3;
    --blue-slate:#1f3a6c;
    --blue-band:#24498e;
    --blue-steel:#28477f;
    --navy-diag:#1f3157;
    --green:#9bcb3c;
    --green-pale:#cadf82;
    --white:#ffffff;
  }
  *{margin:0;padding:0;box-sizing:border-box}
  html,body{width:854px;height:1200px;overflow:hidden;background:var(--navy)}
  .cover{position:relative;width:854px;height:1200px;overflow:hidden}
  .cover-art{position:absolute;inset:0;width:854px;height:1200px}
  .title{font-family:"Alfa Slab One",Georgia,serif;fill:var(--white)}
  .volume-word{font-family:"Roboto Condensed","Arial Narrow",sans-serif;font-weight:700;fill:var(--green)}
  .volume-number{font-family:"Roboto Condensed","Arial Narrow",sans-serif;font-weight:700;fill:var(--white)}
  .features{position:absolute;left:48px;top:1040px;display:flex;gap:0;list-style:none}
  .feature{display:flex;flex-direction:column;align-items:center;text-align:center;
    font-family:Roboto,Arial,sans-serif;font-weight:700;font-size:10.5px;line-height:11px;
    color:var(--white);text-transform:uppercase}
  .feature svg{display:block;height:64px;margin-bottom:10px}
  .brand{position:absolute;left:622px;top:1049px;width:176px;height:54px;
    display:flex;align-items:center;justify-content:center;
    font-family:Roboto,Arial,sans-serif;font-weight:700;font-size:17px;letter-spacing:1px;
    color:var(--white)}
</style>
</head>
<body>
<div class="cover">
  <svg class="cover-art" viewBox="0 0 1067 1500" preserveAspectRatio="none" aria-hidden="false">
    <g class="background">
      <rect width="1067" height="1500" fill="var(--navy)"/>
      <polygon points="0,0 1067,0 1067,660 440,465 270,605 0,430" fill="var(--blue-mid)"/>
      <polygon points="0,0 1067,0 1067,310 0,330" fill="var(--blue-bright)"/>
      <polygon points="620,0 1067,0 1067,90 840,88" fill="var(--blue-sky)"/>
      <polygon points="0,320 270,605 0,830" fill="var(--blue-slate)"/>
      <polygon points="270,605 440,465 1067,660 1067,740 700,860" fill="var(--blue-band)"/>
      <polygon points="700,860 1067,740 1067,1080 885,980" fill="var(--blue-steel)"/>
      <polygon points="0,830 270,605 885,980 0,1070" fill="var(--navy-diag)"/>
      <polygon points="0,1500 1067,865 1067,1500" fill="var(--navy-deep)"/>
    </g>
    <g class="title-banner">
      <polygon points="50,87 1055,87 930,437 130,437" fill="var(--green)"/>
      <polygon points="1055,87 1067,84 1067,372 930,437" fill="var(--green-pale)"/>
      <text class="title" x="125" y="282" font-size="230" textLength="815" lengthAdjust="spacingAndGlyphs">Physics</text>
    </g>
    <g class="volume-badge">
      <polygon points="649,312 973,312 939,407 649,407" fill="var(--white)"/>
      <text class="volume-word" x="670" y="389" font-size="84" textLength="104" lengthAdjust="spacingAndGlyphs">Vol</text>
      <rect x="797" y="323" width="65" height="74" fill="var(--green)"/>
      <text class="volume-number" x="829.5" y="389" font-size="80" text-anchor="middle">1</text>
    </g>
  </svg>

  <ul class="features">
    <li class="feature" style="width:100px">
      <svg viewBox="0 0 110 74" width="98" aria-hidden="true">
        <path d="M28 2a26 22 0 1 1-8 41l-12 12 4-16A26 22 0 0 1 28 2z" fill="#fff"/>
        <text x="26" y="32" font-family="Roboto,Arial,sans-serif" font-weight="700" font-size="26" fill="#1c2a48" text-anchor="middle">?</text>
        <path d="M72 18a33 27 0 1 1-6 53l-6 2 4-8A33 27 0 0 1 72 18z" fill="#fff" stroke="#1c2a48" stroke-width="3"/>
        <rect x="60" y="34" width="22" height="20" fill="none" stroke="#1c2a48" stroke-width="3"/>
        <path d="M65 44l6 6 14-16" fill="none" stroke="#1c2a48" stroke-width="3.5"/>
      </svg>
      Questions &amp;<br>Answers
    </li>
    <li class="feature" style="width:112px">
      <svg viewBox="0 0 60 62" width="56" aria-hidden="true">
        <path d="M4 12l36-8 10 50-36 8z" fill="#fff"/>
        <path d="M8 10l34-4 6 48-34 4z" fill="#fff" stroke="#1c2a48" stroke-width="2"/>
        <g stroke="#1c2a48" stroke-width="2"><path d="M14 18l22-3M15 26l22-3M16 34l22-3M17 42l22-3M18 50l22-3"/></g>
        <path d="M30 40l22-30 6 4-22 30-8 4z" fill="#fff" stroke="#1c2a48" stroke-width="2"/>
      </svg>
      Theory<br>Notes
    </li>
    <li class="feature" style="width:96px">
      <svg viewBox="0 0 54 66" width="52" aria-hidden="true">
        <rect x="0" y="6" width="54" height="60" fill="#fff"/>
        <path d="M27 0v14" stroke="#1c2a48" stroke-width="2"/>
        <path d="M27 28c-9 0-12 8-10 14 2 5 5 7 5 11h10c0-4 3-6 5-11 2-6-1-14-10-14z" fill="none" stroke="#1c2a48" stroke-width="2.5"/>
        <rect x="22" y="18" width="10" height="9" fill="none" stroke="#1c2a48" stroke-width="2"/>
      </svg>
      Tips &amp;<br>Tricks
    </li>
    <li class="feature" style="width:110px">
      <svg viewBox="0 0 60 66" width="56" aria-hidden="true">
        <circle cx="24" cy="22" r="17" fill="none" stroke="#fff" stroke-width="5"/>
        <path d="M24 12v11h9" fill="none" stroke="#fff" stroke-width="4"/>
        <g font-family="Roboto,Arial,sans-serif" font-weight="700" fill="#fff">
          <text x="44" y="36" font-size="16">?</text>
          <text x="30" y="52" font-size="18">?</text>
          <text x="16" y="64" font-size="20">?</text>
        </g>
      </svg>
      Previous Year's<br>Reference<br>Questions
    </li>
    <li class="feature" style="width:96px">
      <svg viewBox="0 0 64 64" width="60" aria-hidden="true">
        <path d="M10 40a24 24 0 0 0 42 8l6 4 0-16-14 4 5 3a18 18 0 0 1-33-3z" fill="#fff"/>
        <path d="M54 24a24 24 0 0 0-42-8l-6-4 0 16 14-4-5-3a18 18 0 0 1 33 3z" fill="#fff"/>
        <path d="M22 14l20 6-6 22-20-6z" fill="#fff" stroke="#1c2a48" stroke-width="2"/>
        <path d="M26 20l12 4" stroke="#1c2a48" stroke-width="2"/>
      </svg>
      Covers<br>Complete<br>Syllabus
    </li>
  </ul>

  <div class="brand">VORLIN EDUCATION</div>
</div>
</body>
</html>
```